Business Cards

Business card design for my company.
I would like the card's background colour to be black. You can also see our web site to get an idea of our brand. https://www.tmwhomecrafting.com.au/
- Name
- Email

```html
<!DOCTYPE html>
<html lang="en">
<head>
<meta charset="utf-8">
<title>TMW Home Crafting – Business Cards</title>
<link rel="stylesheet" href="https://fonts.googleapis.com/css2?family=Montserrat:wght@400;500;700&display=swap">
<style>
  :root {
    --stage: #141414;
    --card: #1f1f1f;
    --card-back-top: #2a2a2a;
    --card-back-bottom: #141414;
    --green: #1f9a45;
    --white: #f4f4f4;
    --muted: #d9d9d9;
  }
  * { margin: 0; padding: 0; box-sizing: border-box; }
  html, body { width: 1200px; height: 900px; overflow: hidden; }
  body {
    background: var(--stage);
    font-family: "Montserrat", sans-serif;
    position: relative;
  }
  .card {
    position: absolute;
    width: 600px;
    height: 343px;
    border-radius: 18px;
    overflow: hidden;
    box-shadow: 0 18px 40px rgba(0,0,0,.55);
  }
  /* Back side */
  .card-back { left: 90px; top: 70px; background: var(--card); }
  .card-back .pattern-fill {
    position: absolute; inset: 0;
    background: linear-gradient(120deg, var(--card-back-bottom) 0%, var(--card-back-top) 100%);
  }
  .card-back .brand-mark {
    position: absolute; right: 34px; bottom: 40px;
    display: flex; align-items: center; gap: 8px;
    color: var(--white); font-weight: 700; font-size: 14px; letter-spacing: .12em;
  }
  .brand-square { background: var(--green); display: inline-block; }
  .card-back .brand-square { width: 12px; height: 12px; }

  /* Front side */
  .card-front { left: 510px; top: 480px; background: var(--card); }
  .card-front .brand-mark {
    position: absolute; right: 36px; top: 44px;
    display: flex; align-items: center; gap: 12px;
    color: var(--white); font-weight: 700; font-size: 24px; letter-spacing: .1em;
  }
  .card-front .brand-square { width: 22px; height: 22px; }
  .contact-block { position: absolute; left: 44px; bottom: 38px; }
  .person-name { color: var(--green); font-weight: 700; font-size: 30px; line-height: 1.1; }
  .person-role { color: var(--white); font-weight: 400; font-size: 17px; margin: 4px 0 20px 8px; }
  .contact-list { list-style: none; margin-left: 8px; }
  .contact-list li {
    display: flex; align-items: center; gap: 12px;
    color: var(--white); font-size: 17px; font-weight: 400; line-height: 1.75;
  }
  .contact-list svg { width: 15px; height: 15px; flex: none; }
</style>
</head>
<body>

  <section class="card card-back" aria-label="Business card, back">
    <div class="pattern-fill" role="img" aria-label="Tonal repeating brand pattern across the card"></div>
    <div class="brand-mark"><span class="brand-square"></span>TMW HOME CRAFTING</div>
  </section>

  <section class="card card-front" aria-label="Business card, front">
    <div class="brand-mark"><span class="brand-square"></span>TMW HOME CRAFTING</div>

    <div class="contact-block">
      <h1 class="person-name">Liam Carver</h1>
      <p class="person-role">General Manager</p>
      <ul class="contact-list">
        <li>
          <svg viewBox="0 0 24 24" aria-hidden="true"><path fill="#1f9a45" d="M6.6 10.8a15.1 15.1 0 0 0 6.6 6.6l2.2-2.2a1 1 0 0 1 1-.25 11.4 11.4 0 0 0 3.6.57 1 1 0 0 1 1 1V20a1 1 0 0 1-1 1A17 17 0 0 1 3 4a1 1 0 0 1 1-1h3.5a1 1 0 0 1 1 1c0 1.25.2 2.45.57 3.57a1 1 0 0 1-.25 1z"/></svg>
          0400 123 456
        </li>
        <li>
          <svg viewBox="0 0 24 24" aria-hidden="true"><rect x="2" y="5" width="20" height="14" rx="1.5" fill="#1f9a45"/><path d="M3 6l9 7 9-7" fill="none" stroke="#1f1f1f" stroke-width="1.8"/></svg>
          liam@tmwhomecrafting.com.au
        </li>
        <li>
          <svg viewBox="0 0 24 24" aria-hidden="true"><g fill="none" stroke="#1f9a45" stroke-width="2"><circle cx="12" cy="12" r="9.5"/><ellipse cx="12" cy="12" rx="4.2" ry="9.5"/><path d="M2.5 12h19M4 7h16M4 17h16"/></g></svg>
          www.tmwhomecrafting.com.au
        </li>
      </ul>
    </div>
  </section>

</body>
</html>
```